Post Lockdown Ortho Special

We are running a special for (Ortho) Braces/Clear Aligner (Quorventa), till July 31st 2020. Up to $2,000 off with free Consultation and Xrays.

We need a ad to run in different formats.

Maybe something with: what better time to get braces when you have to wear a mask all the time.

Trying to rebuild our business and get people in for free consultations.

```html
<!DOCTYPE html>
<html lang="en">
<head>
<meta charset="utf-8">
<title>Ridgeline Family Dentistry – Post Lockdown Ortho Special</title>
<link href="https://fonts.googleapis.com/css2?family=Arimo:wght@700&family=Jost:wght@300;400;500;600;700&display=swap" rel="stylesheet">
<style>
  :root {
    --page: #ffffff;
    --bg-pink: #f3dcdc;
    --bg-mauve: #c29bbd;
    --bg-purple: #7c4fa6;
    --headline: #6b3f98;
    --headline-shadow: #3e2160;
    --free: #8b0d5e;
    --navy: #0d3e6a;
    --plum: #8b0d5e;
    --date: #4a1a2a;
    --frame-line: #ffffff;
    --logo-frame: #4e1d2c;
    --logo-text: #5b2f8a;
    --hex-light: #ffffff;
    --hex-dark: #c9c9cc;
    --photo-top: #a27fb8;
    --photo-bottom: #8a5a8e;
  }
  * { margin: 0; padding: 0; box-sizing: border-box; }
  html, body { width: 1200px; height: 650px; overflow: hidden; background: var(--page); }
  .canvas { position: relative; width: 1200px; height: 650px; }
  .ad {
    position: absolute; left: 108px; top: 55px; width: 985px; height: 517px; overflow: hidden;
    background: linear-gradient(115deg, var(--bg-pink) 0%, var(--bg-mauve) 45%, var(--bg-purple) 100%);
  }
  .bokeh { position: absolute; inset: 0; }
  .headline {
    position: absolute; left: 54px; top: 69px;
    font-family: "Arimo", Arial, sans-serif; font-weight: 700; color: var(--headline);
    text-shadow: 1px 2px 0 var(--headline-shadow);
    letter-spacing: -0.5px; white-space: nowrap;
  }
  .headline__main { display: block; font-size: 44px; line-height: 48px; }
  .headline__sub { display: block; font-size: 30px; line-height: 40px; }
  .offer-frame { position: absolute; left: 0; top: 0; }
  .free-label {
    position: absolute; left: 163px; top: 197px; width: 130px; text-align: center;
    font-family: "Jost", sans-serif; font-weight: 700; font-size: 52px; line-height: 1;
    color: var(--free); text-shadow: 2px 2px 0 #fff;
  }
  .hex-label {
    position: absolute; width: 108px; text-align: center;
    font-family: "Jost", sans-serif; font-weight: 500; color: var(--navy);
  }
  .hex-label--consult { left: 107px; top: 320px; font-size: 22px; }
  .hex-label--xray { left: 231px; top: 317px; font-size: 25px; }
  .discount {
    position: absolute; left: 500px; top: 227px; width: 150px; text-align: center;
    font-family: "Jost", sans-serif; color: var(--plum); line-height: 1;
  }
  .discount__lead { display: block; font-weight: 300; font-size: 30px; letter-spacing: -1px; }
  .discount__amount { display: block; font-weight: 700; font-size: 29px; margin-top: 4px; }
  .discount__off { display: block; font-weight: 700; font-size: 30px; margin-top: 2px; }
  .deadline {
    position: absolute; left: 498px; top: 347px;
    font-family: "Jost", sans-serif; font-weight: 400; font-size: 21px; color: var(--date);
  }
  .portrait {
    position: absolute; left: 693px; top: 86px; width: 252px; height: 266px;
    background: linear-gradient(180deg, var(--photo-top) 0%, var(--photo-bottom) 100%);
  }
  .practice-badge {
    position: absolute; left: 691px; top: 350px; width: 253px; height: 117px;
    border: 7px solid var(--logo-frame); background: #fff;
    display: flex; align-items: center; gap: 10px; padding: 0 12px;
  }
  .practice-badge__dot { flex: none; width: 14px; height: 14px; border-radius: 50%; background: var(--logo-text); }
  .practice-badge__name {
    font-family: "Jost", sans-serif; font-weight: 500; color: var(--logo-text);
    font-size: 16px; line-height: 1.4; white-space: nowrap;
  }
</style>
</head>
<body>
<div class="canvas">
  <section class="ad">
    <svg class="bokeh" width="985" height="517" aria-hidden="true">
      <circle cx="70" cy="150" r="120" fill="#fff" opacity="0.18"/>
      <circle cx="520" cy="425" r="105" fill="#fff" opacity="0.12"/>
      <circle cx="230" cy="620" r="130" fill="#fff" opacity="0.2"/>
      <circle cx="620" cy="480" r="230" fill="#fff" opacity="0.06"/>
      <circle cx="810" cy="65" r="15" fill="#fff" opacity="0.2"/>
      <circle cx="920" cy="70" r="14" fill="#fff" opacity="0.2"/>
      <circle cx="770" cy="90" r="6" fill="#fff" opacity="0.3"/>
      <circle cx="850" cy="50" r="5" fill="#fff" opacity="0.3"/>
    </svg>

    <h1 class="headline">
      <span class="headline__main">What better time to get braces</span>
      <span class="headline__sub">when you have to wear a mask all the time?</span>
    </h1>

    <svg class="offer-frame" width="985" height="517" aria-hidden="true">
      <polyline points="156,222 57,222 57,332 96,332" fill="none" stroke="var(--frame-line)" stroke-width="3"/>
      <polyline points="300,222 397,222 397,332 354,332" fill="none" stroke="var(--frame-line)" stroke-width="3"/>
      <defs>
        <linearGradient id="hexFill" x1="0" x2="1" y1="0" y2="0">
          <stop offset="0" stop-color="var(--hex-dark)"/>
          <stop offset="1" stop-color="var(--hex-light)"/>
        </linearGradient>
        <linearGradient id="bubbleFill" x1="0" x2="1" y1="0" y2="0">
          <stop offset="0" stop-color="#cfcfd2"/>
          <stop offset="0.6" stop-color="#ffffff"/>
        </linearGradient>
      </defs>
      <polygon points="161,272 215,303 215,365 161,396 107,365 107,303" fill="url(#hexFill)" stroke="#fff" stroke-width="3"/>
      <polygon points="283,272 337,303 337,365 283,396 229,365 229,303" fill="url(#hexFill)" stroke="#fff" stroke-width="3"/>
      <path d="M570,199 C610,194 660,208 720,222 C688,268 640,328 572,338 Z" fill="#fff"/>
      <circle cx="570" cy="269" r="71" fill="#fff"/>
      <circle cx="572" cy="269" r="65" fill="url(#bubbleFill)"/>
    </svg>

    <div class="free-label">FREE</div>
    <div class="hex-label hex-label--consult">Consultant</div>
    <div class="hex-label hex-label--xray">Xray</div>

    <p class="discount">
      <span class="discount__lead">UP TO</span>
      <span class="discount__amount">$2,000</span>
      <span class="discount__off">OFF</span>
    </p>
    <p class="deadline">Till July 31st 2020</p>

    <div class="portrait" role="img" aria-label="Photo of a smiling woman with curly hair and glasses looking at a tablet"></div>

    <div class="practice-badge">
      <span class="practice-badge__dot" aria-hidden="true"></span>
      <p class="practice-badge__name">Ridgeline Family Dentistry<br>Dr Maren Ellsworth</p>
    </div>
  </section>
</div>
</body>
</html>
```